Business Card Design for Event Planning Company

Create a business card for event planning company using our new logo. After I pick the design, I will need files made for 6 employees. Our company provides event design & logistics services as well as venue management. The font should be sans serif and complementary to the logo. I will need to know the name of the font selected for the final design. The phone numbers listed should be separated by "." not "-"

Address for the card
PO Box 318, Washington, DC 20019

Card One
Lorna Pettibone
lpettibone@galavoyant.com
202.481.7730

Card Two
Miriam Okonkwo
mokonkwo@galavoyant.com
202.556.2047

Card Three
Tessa Varnholt
tvarnholt@galavoyant.com
978.620.4471

Card Four
Robin Fess
rfess@galavoyant.com
202.718.3362

Card Five
Ada-Rose Pelletan-Uzor
adarose@galavoyant.com
202.839.1205

Card Six
Beatrix Holloway
Beatrix@galavoyant.com
202.492.6618

Target Market(s)

Corporate/Non-Profit

Industry/Entity Type

Event Planning

Contact Information for Business Card

Address for the card

Card One
Lorna Pettibone
lpettibone@galavoyant.com
202.481.7730

Card Two
Miriam Okonkwo
202.556.2047

Card Three
Tessa Varnholt
978.620.4471

Card Four
Robin Fess
rfess@galavoyant.com
202.718.3362

Card Five
Ada-Rose Pelletan-Uzor
202.839.1205

Card Six
Beatrix Holloway
202.492.6618

Font styles to use
Sans Serif

Colors

Designer to choose colors to be used in the design.

Requirements
Must have
• Two-sided with logo
Should not have
• Extra colors or be too busy

```html
<!DOCTYPE html>
<html lang="en">
<head>
<meta charset="utf-8">
<title>Galavoyant Business Card</title>
<link rel="stylesheet" href="https://fonts.googleapis.com/css2?family=Arimo:wght@400;700&family=Questrial&display=swap">
<style>
  :root {
    --backdrop: #e6e6e4;
    --card-white: #fbfbfa;
    --card-dark: #2b292a;
    --ink-dark: #2a2a2a;
    --ink-light: #ffffff;
    --accent-teal: #5bb3b0;
    --shadow: rgba(0, 0, 0, 0.18);
  }
  * { box-sizing: border-box; margin: 0; padding: 0; }
  html, body {
    width: 1200px;
    height: 900px;
    overflow: hidden;
    background: var(--backdrop);
  }
  .canvas {
    width: 1200px;
    height: 900px;
    display: flex;
    flex-direction: column;
    align-items: center;
    justify-content: center;
    gap: 40px;
  }
  .card {
    width: 680px;
    height: 389px;
    border-radius: 4px;
    box-shadow: 0 10px 30px var(--shadow);
    position: relative;
    overflow: hidden;
  }
  /* Front side */
  .card-front {
    background: var(--card-white);
    display: flex;
    align-items: center;
    justify-content: center;
  }
  .brand {
    display: flex;
    align-items: center;
    gap: 18px;
  }
  .brand-dot {
    width: 34px;
    height: 34px;
    border-radius: 50%;
    background: var(--accent-teal);
  }
  .brand-name {
    font-family: "Questrial", sans-serif;
    font-size: 64px;
    letter-spacing: 1px;
    color: var(--ink-dark);
    line-height: 1;
  }
  /* Back side */
  .card-back {
    background: linear-gradient(160deg, #353334 0%, var(--card-dark) 55%, #242223 100%);
    color: var(--ink-light);
    font-family: "Arimo", sans-serif;
  }
  .back-brand {
    position: absolute;
    top: 46px;
    right: 52px;
    font-family: "Questrial", sans-serif;
    font-size: 34px;
    color: var(--ink-light);
  }
  .contact {
    position: absolute;
    left: 62px;
    bottom: 44px;
  }
  .contact-name {
    font-weight: 700;
    font-size: 22px;
    letter-spacing: 0.5px;
    text-transform: uppercase;
    margin-bottom: 10px;
  }
  .contact-address {
    font-size: 15px;
    line-height: 1.3;
    margin-bottom: 8px;
  }
  .contact-list {
    list-style: none;
    font-size: 15px;
    line-height: 1.35;
  }
  .contact-list li {
    display: flex;
    align-items: center;
    gap: 10px;
  }
  .contact-icon {
    width: 13px;
    height: 13px;
    flex: none;
  }
</style>
</head>
<body>
  <main class="canvas">
    <section class="card card-front" aria-label="Card front">
      <div class="brand">
        <span class="brand-dot"></span>
        <span class="brand-name">galavoyant</span>
      </div>
    </section>

    <section class="card card-back" aria-label="Card back">
      <div class="back-brand">galavoyant</div>
      <div class="contact">
        <p class="contact-name">Lorna Pettibone</p>
        <p class="contact-address">PO Box 318, Washington<br>DC 20019</p>
        <ul class="contact-list">
          <li>
            <svg class="contact-icon" viewBox="0 0 13 13" aria-hidden="true">
              <rect x="3" y="0.75" width="7" height="11.5" rx="1.2" fill="none" stroke="#fff" stroke-width="1.4"/>
              <circle cx="6.5" cy="10" r="0.8" fill="#fff"/>
            </svg>
            <span>202.481.7730</span>
          </li>
          <li>
            <svg class="contact-icon" viewBox="0 0 13 13" aria-hidden="true">
              <rect x="0.5" y="2.5" width="12" height="8" fill="#fff"/>
              <path d="M0.5 2.5 L6.5 7.2 L12.5 2.5" fill="none" stroke="#2b292a" stroke-width="1.1"/>
            </svg>
            <span>lpettibone@galavoyant.com</span>
          </li>
          <li>
            <svg class="contact-icon" viewBox="0 0 13 13" aria-hidden="true">
              <circle cx="6.5" cy="6.5" r="5.8" fill="#fff"/>
              <path d="M1 6.5 H12 M6.5 0.8 C3.8 3.5 3.8 9.5 6.5 12.2 M6.5 0.8 C9.2 3.5 9.2 9.5 6.5 12.2" fill="none" stroke="#2b292a" stroke-width="0.9"/>
            </svg>
            <span>www.galavoyant.com</span>
          </li>
        </ul>
      </div>
    </section>
  </main>
</body>
</html>
```